Gift voucher for a photo shoot, folding card DIN long (21 x 9.8 cm)

Hello, I'm a professional photographer and need a new design for my gift voucher card for a photo shoot. The design should be applicable to all types of photo shoots (neutral). I prefer a sophisticated design. The folded card should be printed on both sides.
My data should be included: Logo, Address: Wendtaler Gasse 9, 07318 Gera, Email: fotograf@jonasbirkner.eu, Website: www.jonasbirkner.eu Tel.: 0176 / 4389025
Updates

Please design the folding card in DIN long format (105 x 210 mm, landscape format). The card should open horizontally. Please design the front with the words "Gift voucher for you" and my logo. Please make the logo small – the words "Gift voucher" should be in the foreground.
The colors - use elegant gray with gold or white font color.
The inside should contain the words: Photo shoot for ........ worth .....€, as well as my logo.
My contact details should be on the back.

Target Market(s)

Private customer

Colors

Designer to choose only greyscale colors for use in the design.

Requirements
Must have
• Noble appearance, a gift voucher that one likes to give away, words: Gift voucher for you, photo shoot for ..., worth .......€
Nice to have
• Noble appearance of the gift voucher, a gift voucher that you like to give away
Should not have
• no pictures

```html
<!DOCTYPE html>
<html lang="de">
<head>
<meta charset="utf-8">
<title>Jonas Birkner – Gift Voucher Folding Card</title>
<link rel="stylesheet" href="https://fonts.googleapis.com/css2?family=Montserrat:wght@300;400;600&display=swap">
<style>
  :root {
    --backdrop: #e3e3e3;
    --panel-deep: #161816;
    --panel-cover: #2c2d2d;
    --panel-inner-left: #252626;
    --panel-inner-right: #1c1d1c;
    --silver: #c9c9c9;
    --silver-soft: #a9a9a9;
    --silver-faint: rgba(200, 200, 200, 0.2);
    --white: #f2f2f2;
    --fold-line: rgba(0, 0, 0, 0.45);
    --field-line: rgba(200, 200, 200, 0.55);
  }
  * { box-sizing: border-box; margin: 0; padding: 0; }
  html, body {
    width: 848px;
    height: 1200px;
    overflow: hidden;
    background: var(--backdrop);
    font-family: "Montserrat", Helvetica, Arial, sans-serif;
  }
  .sheet { position: relative; width: 848px; height: 1200px; }
  .spread {
    position: absolute;
    left: 85px;
    width: 678px;
    height: 232px;
    display: flex;
    box-shadow: 0 6px 18px rgba(0, 0, 0, 0.18);
  }
  .spread--outside { top: 330px; }
  .spread--inside { top: 660px; }
  .panel { position: relative; width: 50%; height: 100%; overflow: hidden; }
  .panel + .panel { border-left: 1px solid var(--fold-line); }

  .panel--back { background: var(--panel-deep); }
  .panel--cover {
    background: var(--panel-cover);
    display: flex;
    flex-direction: column;
    align-items: center;
    justify-content: center;
  }
  .brand-mark { width: 40px; height: 40px; margin-bottom: 8px; }
  .brand-name {
    font-weight: 400;
    font-size: 14px;
    letter-spacing: 0.08em;
    color: var(--silver);
    text-transform: uppercase;
    line-height: 1;
  }
  .brand-role {
    margin-top: 4px;
    font-weight: 600;
    font-size: 8px;
    letter-spacing: 0.28em;
    color: var(--silver-soft);
  }
  .voucher-title {
    margin-top: 16px;
    font-weight: 400;
    font-size: 24px;
    letter-spacing: 0.1em;
    line-height: 1.1;
    color: var(--white);
    text-transform: uppercase;
    text-align: center;
  }
  .voucher-subtitle {
    margin-top: 4px;
    font-weight: 300;
    font-size: 11px;
    letter-spacing: 0.2em;
    color: var(--silver-soft);
    text-transform: uppercase;
  }

  .panel--inner-left { background: var(--panel-inner-left); }
  .watermark-ring {
    position: absolute;
    left: -14px;
    top: 26px;
    width: 150px;
    height: 150px;
  }
  .watermark-name {
    position: absolute;
    left: 0;
    width: 122px;
    top: 94px;
    text-align: center;
    font-weight: 400;
    font-size: 11px;
    letter-spacing: 0.06em;
    text-transform: uppercase;
    color: var(--silver-faint);
  }
  .voucher-fields {
    position: absolute;
    left: 156px;
    right: 22px;
    top: 72px;
    display: flex;
    flex-direction: column;
    gap: 26px;
  }
  .field {
    display: flex;
    align-items: flex-end;
    gap: 6px;
    font-weight: 300;
    font-size: 10px;
    letter-spacing: 0.06em;
    color: var(--silver);
  }
  .field__label { white-space: nowrap; }
  .field__blank {
    flex: 1;
    border-bottom: 1px dotted var(--field-line);
    height: 10px;
  }

  .panel--contact {
    background: var(--panel-inner-right);
    display: flex;
    align-items: center;
    justify-content: flex-end;
    padding-right: 46px;
  }
  .contact { text-align: center; font-style: normal; }
  .contact__name {
    font-weight: 600;
    font-size: 10px;
    letter-spacing: 0.05em;
    color: var(--white);
    margin-bottom: 9px;
  }
  .contact__line {
    font-weight: 300;
    font-size: 8px;
    letter-spacing: 0.06em;
    line-height: 1.45;
    color: var(--silver);
  }
</style>
</head>
<body>
<main class="sheet">

  <section class="spread spread--outside" aria-label="Outside of the folding card">
    <div class="panel panel--back"></div>
    <div class="panel panel--cover">
      <svg class="brand-mark" viewBox="0 0 40 40" aria-hidden="true">
        <circle cx="20" cy="20" r="18" fill="none" stroke="#d6d6d6" stroke-width="1.5"/>
      </svg>
      <p class="brand-name">Jonas Birkner</p>
      <p class="brand-role">FOTOGRAF</p>
      <h1 class="voucher-title">Gift Voucher</h1>
      <p class="voucher-subtitle">for you</p>
    </div>
  </section>

  <section class="spread spread--inside" aria-label="Inside of the folding card">
    <div class="panel panel--inner-left">
      <svg class="watermark-ring" viewBox="0 0 150 150" aria-hidden="true">
        <circle cx="75" cy="75" r="72" fill="none" stroke="rgba(200,200,200,0.2)" stroke-width="2"/>
      </svg>
      <p class="watermark-name">Jonas Birkner</p>
      <div class="voucher-fields">
        <p class="field"><span class="field__label">Photo shoot for</span><span class="field__blank"></span></p>
        <p class="field"><span class="field__label">worth</span><span class="field__blank"></span><span class="field__label">€</span></p>
      </div>
    </div>
    <div class="panel panel--contact">
      <address class="contact">
        <p class="contact__name">Jonas Birkner</p>
        <p class="contact__line">Wendtaler Gasse 9, 07318 Gera</p>
        <p class="contact__line">Email: fotograf@jonasbirkner.eu</p>
        <p class="contact__line">Tel.: 0176 / 4389025</p>
        <p class="contact__line">www.jonasbirkner.eu</p>
      </address>
    </div>
  </section>

</main>
</body>
</html>
```